Zielgruppe
Wir produzieren Rebuilt Toner Kartuschen und vertreiben diese an privat Anwender und auch Firmen Kunden.
Unsere Produkte vertreiben wir unter einer eigenen Marke und auch neutral an Wiederverkäufer.
Jetzt suchen wir ein neues Produkt Aufkleber Design für die neutrale Ware (ohne Logo) soll aber trotzdem ein Wiedererkennungswert haben, aber nicht direkt auf uns zurückführen.
Ein Bild vom aktuellen Aufkleber, ist anbei.
Aufgabenstellung
Es soll ein universal Design sein welches wir für alle Produkte verwenden können. Somit keine Artikel Informationen im Design.
Als Text soll 'Rebuilt Cartridge' und 'Made in Germany' verwendet werden.
Das Design soll die hohe Qualität unterstreichen.
Die Hintergrundfarbe soll Schwarz sein.
Der Standard Aufkleber soll die Abmessungen 233x84mm haben.

```html
<!DOCTYPE html>
<html lang="de">
<head>
<meta charset="utf-8">
<title>Rebuilt Cartridge – Etikett</title>
<link href="https://fonts.googleapis.com/css2?family=Allura&family=Roboto:wght@300;400&display=swap" rel="stylesheet">
<style>
  :root {
    --paper: #ffffff;
    --label-black: #000000;
    --ink-white: #ffffff;
  }
  html, body {
    margin: 0;
    padding: 0;
    width: 1200px;
    height: 462px;
    overflow: hidden;
    background: var(--paper);
  }
  .label {
    position: relative;
    width: 1200px;
    height: 462px;
  }
  .label-art {
    position: absolute;
    inset: 0;
  }
  .label-text {
    position: absolute;
    left: 546px;
    top: 0;
    transform: translateX(-50%);
    text-align: center;
    color: var(--ink-white);
    white-space: nowrap;
  }
  .tagline {
    position: absolute;
    left: 50%;
    top: 108px;
    transform: translateX(-50%);
    margin: 0;
    font-family: "Allura", cursive;
    font-size: 64px;
    line-height: 1;
    font-weight: 400;
  }
  .product-name {
    position: absolute;
    left: 50%;
    top: 182px;
    transform: translateX(-50%);
    margin: 0;
    font-family: "Roboto", sans-serif;
    font-weight: 300;
    font-size: 94px;
    line-height: 1;
    font-variant: small-caps;
    letter-spacing: 1px;
  }
  .origin {
    position: absolute;
    left: 50%;
    top: 322px;
    transform: translateX(-50%);
    margin: 0;
    font-family: "Roboto", sans-serif;
    font-weight: 400;
    font-size: 20px;
    line-height: 1;
  }
</style>
</head>
<body>
  <main class="label">
    <svg class="label-art" width="1200" height="462" viewBox="0 0 1200 462" aria-hidden="true">
      <rect class="label-ground" x="24" y="21" width="1152" height="419" fill="var(--label-black)"/>
      <polyline class="label-frame" points="46,46 1154,46 1154,262 946,415 46,415 46,46"
                fill="none" stroke="var(--ink-white)" stroke-width="8" stroke-linejoin="miter"/>
      <path class="corner-accent" d="M1152,284 Q1152,274 1144,280 L996,410 Q990,416 998,416 L1146,416 Q1152,416 1152,410 Z"
            fill="var(--ink-white)"/>
    </svg>
    <div class="label-text">
      <p class="tagline">Premium</p>
      <h1 class="product-name">Rebuilt Cartridge</h1>
      <p class="origin">Made in Germany</p>
    </div>
  </main>
</body>
</html>
```